A simple Chatterbook Ad (not Chatterbook Page) for weight loss surgery

It’s a simple ad in terms of the text.

The text should say:
Curious about weight loss surgery?
This 30 second quiz will tell you which procedure will suit you best

I'm open to variations in the text if it is thought to enhance the ad.

Targeted towards obese individuals who have been unable to lose weight with diet and exercise. My industry is weight loss surgery – webpage www.marcusbellweather.com.au. Clicking the ad leads to a quiz on my webpage relating to weight loss surgery. Most frequent users of this service are females (75%) between ages of 35 and 55 years.

Successful weight loss surgery can enable individuals who have been unable to lose weight to lose a substantial amount of the excess weight they are carrying to be healthier and happier.

```html
<!DOCTYPE html>
<html lang="en">
<head>
<meta charset="utf-8">
<title>Weight Loss Surgery Quiz – Chatterbook Ad</title>
<link rel="stylesheet" href="https://fonts.googleapis.com/css2?family=Montserrat:wght@400;500;600;700;800;900&family=Roboto:wght@400;500;700&family=Tinos&display=swap">
<style>
  :root {
    --board: #a1a7a7;
    --white: #ffffff;
    --ink: #050505;
    --muted: #65676b;
    --bar: #f0f2f5;
    --rule: #ced0d4;
    --teal-deep: #12d9c6;
    --teal-light: #42efe2;
    --brand-teal: #1a9a92;
    --brand-grey: #6d7474;
    --photo-a: #b8a3e0;
    --photo-b: #8e7acb;
    --like-blue: #1877f2;
    --love-red: #f33e58;
  }
  * { box-sizing: border-box; margin: 0; padding: 0; }
  html, body { width: 1200px; height: 2351px; overflow: hidden; }
  body { background: var(--board); position: relative; font-family: "Roboto", Arial, sans-serif; }

  /* ---------- feed post ---------- */
  .post {
    position: absolute; left: 193px; top: 179px; width: 816px; height: 915px;
    background: var(--white); border-radius: 6px; overflow: hidden;
    box-shadow: 0 13px 0 -2px #5c6060;
  }
  .post-header { position: absolute; left: 0; top: 0; width: 100%; height: 142px; border-bottom: 2px solid #7fd3bf; }
  .post-avatar { position: absolute; left: 20px; top: 20px; width: 47px; height: 47px; border-radius: 50%; background: #e4e6e6; }
  .post-name { position: absolute; left: 77px; top: 21px; font-size: 18px; font-weight: 500; color: var(--ink); }
  .post-meta { position: absolute; left: 77px; top: 47px; font-size: 15px; color: var(--muted); display: flex; align-items: center; gap: 4px; }
  .post-meta svg { width: 13px; height: 13px; }
  .post-more { position: absolute; right: 30px; top: 28px; display: flex; gap: 3px; }
  .post-more span { width: 5px; height: 5px; border-radius: 50%; background: #606770; }
  .post-caption { position: absolute; left: 20px; top: 76px; width: 780px; font-size: 17px; line-height: 24px; color: var(--ink); }

  .post-media {
    position: absolute; left: 0; top: 142px; width: 816px; height: 570px; overflow: hidden;
    background: linear-gradient(var(--white) 0 112px, transparent 112px),
                linear-gradient(135deg, var(--teal-deep), var(--teal-light));
  }
  .post-media .ad-art { position: absolute; left: 38px; top: 0; transform: scale(0.7); transform-origin: 0 0; }
  .post-media .ad-photo { left: 640px; top: 130px; width: 330px; }

  .link-bar { position: absolute; left: 0; top: 712px; width: 100%; height: 95px; background: var(--bar); }
  .link-domain { position: absolute; left: 24px; top: 12px; font-size: 14px; color: var(--muted); }
  .link-title { position: absolute; left: 24px; top: 36px; font-size: 19px; font-weight: 700; color: var(--ink); }
  .link-desc { position: absolute; left: 24px; top: 63px; font-size: 17px; color: var(--muted); }
  .link-cta {
    position: absolute; left: 670px; top: 25px; width: 124px; height: 43px; border-radius: 6px;
    background: #e4e6eb; font-size: 16px; font-weight: 500; color: var(--ink);
    display: flex; align-items: center; justify-content: center;
  }

  .reactions { position: absolute; left: 20px; top: 825px; width: 776px; display: flex; align-items: center; font-size: 17px; color: var(--muted); }
  .reaction { width: 22px; height: 22px; border-radius: 50%; border: 2px solid var(--white); }
  .reaction--like { background: var(--like-blue); }
  .reaction--love { background: var(--love-red); margin-left: -4px; margin-right: 8px; }
  .reactions-count { margin-left: auto; }
  .post-divider { position: absolute; left: 19px; top: 861px; width: 777px; height: 1px; background: var(--rule); }
  .actions { position: absolute; left: 0; top: 872px; width: 100%; height: 30px; }
  .action { position: absolute; top: 0; display: flex; align-items: center; gap: 8px; font-size: 18px; font-weight: 500; color: var(--muted); }
  .action svg { width: 22px; height: 22px; fill: none; stroke: var(--muted); stroke-width: 1.8; stroke-linejoin: round; stroke-linecap: round; }
  .action--like { left: 102px; }
  .action--comment { left: 317px; }
  .action--share { left: 574px; }
  .action--audience { left: 745px; gap: 4px; }
  .audience-dot { width: 24px; height: 24px; border-radius: 50%; background: radial-gradient(circle at 40% 40%, #b9a9c9, #4a3f5e); }
  .caret { width: 0; height: 0; border-left: 5px solid transparent; border-right: 5px solid transparent; border-top: 5px solid var(--muted); }

  /* ---------- flat ad ---------- */
  .ad-flat {
    position: absolute; left: 210px; top: 1307px; width: 813px; height: 813px; overflow: hidden;
    box-shadow: 0 18px 30px rgba(0,0,0,.28);
  }
  .ad-art { position: absolute; left: 0; top: 0; width: 813px; height: 813px; font-family: "Montserrat", Arial, sans-serif; color: var(--ink); }
  .ad-band { position: absolute; left: 0; top: 0; width: 100%; height: 159px; background: var(--white); }
  .ad-field { position: absolute; left: 0; top: 159px; width: 100%; height: 654px; background: linear-gradient(135deg, var(--teal-deep), var(--teal-light)); }
  .ad-flat .ad-art { background: none; }

  .brand { position: absolute; left: 50px; top: 44px; display: flex; align-items: center; gap: 16px; }
  .brand-mark { width: 78px; height: 78px; border-radius: 50%; background: var(--brand-teal); }
  .brand-name { font-size: 31px; font-weight: 600; letter-spacing: 1px; text-transform: uppercase; color: var(--brand-teal); line-height: 1; }
  .brand-role { margin-top: 8px; font-family: "Tinos", serif; font-size: 12px; letter-spacing: 2.6px; text-transform: uppercase; color: var(--brand-grey); }

  .ad-photo {
    position: absolute; left: 462px; top: 118px; width: 351px; height: 695px;
    border-radius: 170px 170px 0 0;
    background: linear-gradient(180deg, rgba(255,255,255,.25), var(--photo-a) 45%, var(--photo-b));
  }

  .kicker { position: absolute; left: 50px; top: 229px; font-size: 28px; font-weight: 500; letter-spacing: .2px; }
  .headline { position: absolute; left: 48px; font-size: 76px; font-weight: 900; line-height: 1; letter-spacing: -1px; }
  .headline--one { top: 276px; }
  .headline--two { top: 354px; }
  .headline-tag { position: absolute; left: 262px; top: 366px; height: 39px; padding: 0 10px; background: var(--ink); color: var(--white); font-size: 26px; font-weight: 800; line-height: 39px; }

  .quiz-rule { position: absolute; left: 59px; width: 362px; height: 1px; background: linear-gradient(90deg, transparent, rgba(0,0,0,.25) 20%, rgba(0,0,0,.25) 80%, transparent); }
  .quiz-rule--top { top: 471px; }
  .quiz-rule--bottom { top: 585px; }
  .timer { position: absolute; left: 58px; top: 488px; width: 70px; height: 70px; }
  .timer svg { position: absolute; inset: 0; }
  .timer-value { position: absolute; left: 0; top: 15px; width: 100%; text-align: center; font-size: 28px; font-weight: 800; line-height: 1; }
  .timer-unit { position: absolute; left: 0; top: 44px; width: 100%; text-align: center; font-size: 9px; font-weight: 700; }
  .quiz-copy { position: absolute; left: 144px; top: 486px; font-size: 20px; line-height: 27px; }
  .quiz-copy b { font-weight: 800; }

  .contact-label { position: absolute; left: 62px; top: 640px; font-family: "Tinos", serif; font-size: 24px; }
  .contact-phone { position: absolute; left: 61px; top: 670px; font-size: 45px; font-weight: 900; letter-spacing: .5px; line-height: 1.1; }
  .contact-web { position: absolute; left: 62px; top: 716px; font-family: "Tinos", serif; font-size: 28px; }
</style>
</head>
<body>

<article class="post">
  <header class="post-header">
    <div class="post-avatar"></div>
    <div class="post-name">Marcus Bellweather</div>
    <div class="post-meta">Sponsored ·
      <svg viewBox="0 0 16 16"><circle cx="8" cy="8" r="7" fill="#65676b"/><path d="M3 6c2 0 3 1 3 3s2 2 2 4M9 2c0 2 2 2 3 3s2 1 3 0" stroke="#fff" stroke-width="1.3" fill="none"/></svg>
    </div>
    <div class="post-more"><span></span><span></span><span></span></div>
    <p class="post-caption">Successful weight loss surgery can enable individuals who have been unable to lose weight to lose a substantial amount of the excess weight they are carrying to be healthier and happier.</p>
  </header>

  <div class="post-media">
    <div class="ad-art">
      <div class="brand">
        <div class="brand-mark"></div>
        <div>
          <div class="brand-name">Marcus Bellweather</div>
          <div class="brand-role">General, Upper GI &amp; Bariatric Surgeon</div>
        </div>
      </div>
      <div class="ad-photo" role="img" aria-label="Side profile photo of a woman in purple sportswear with a drawn outline and arrows showing a slimmer silhouette"></div>
      <div class="kicker">CURIOUS ABOUT</div>
      <div class="headline headline--one">WEIGHT</div>
      <div class="headline headline--two">LOSS</div>
      <div class="headline-tag">SURGERY?</div>
      <div class="quiz-rule quiz-rule--top"></div>
      <div class="timer">
        <svg viewBox="0 0 70 70"><circle cx="35" cy="35" r="32" fill="none" stroke="#050505" stroke-width="2" stroke-dasharray="1.5 3.5"/></svg>
        <div class="timer-value">30</div><div class="timer-unit">SEC</div>
      </div>
      <p class="quiz-copy">This <b>30 second</b> quiz<br>will tell you which procedure<br>will <b>suit you best</b></p>
      <div class="quiz-rule quiz-rule--bottom"></div>
      <div class="contact-label">For all appointments</div>
      <div class="contact-phone">03 9000 4127</div>
      <div class="contact-web">www.marcusbellweather.com.au</div>
    </div>
  </div>

  <div class="link-bar">
    <div class="link-domain">www.marcusbellweather.com.au</div>
    <div class="link-title">Curious about weight loss surgery?</div>
    <div class="link-desc">This 30 second quiz will tell you which procedure will suit you best</div>
    <div class="link-cta">Learn more</div>
  </div>

  <div class="reactions">
    <span class="reaction reaction--like"></span><span class="reaction reaction--love"></span>
    <span>Username, Username and 2K others</span>
    <span class="reactions-count">26 Comments&nbsp; 2 Shares</span>
  </div>
  <div class="post-divider"></div>
  <nav class="actions">
    <div class="action action--like"><svg viewBox="0 0 24 24"><path d="M3 10h4v11H3zM7 10l4-7c2 0 3 1 2 4l-1 3h7c1.5 0 2.5 1 2 2.5l-2 7c-.4 1-1 1.5-2 1.5H7"/></svg>Like</div>
    <div class="action action--comment"><svg viewBox="0 0 24 24"><path d="M4 4h16v12H9l-5 4z"/></svg>Comment</div>
    <div class="action action--share"><svg viewBox="0 0 24 24"><path d="M13 5l8 7-8 7v-4c-5 0-8 1-10 5 0-6 3-10 10-11z"/></svg>Share</div>
    <div class="action action--audience"><span class="audience-dot"></span><span class="caret"></span></div>
  </nav>
</article>

<section class="ad-flat">
  <div class="ad-art">
    <div class="ad-band"></div>
    <div class="ad-field"></div>
    <div class="brand">
      <div class="brand-mark"></div>
      <div>
        <div class="brand-name">Marcus Bellweather</div>
        <div class="brand-role">General, Upper GI &amp; Bariatric Surgeon</div>
      </div>
    </div>
    <div class="ad-photo" role="img" aria-label="Side profile photo of a woman in purple sportswear with a drawn outline and arrows showing a slimmer silhouette"></div>
    <div class="kicker">CURIOUS ABOUT</div>
    <div class="headline headline--one">WEIGHT</div>
    <div class="headline headline--two">LOSS</div>
    <div class="headline-tag">SURGERY?</div>
    <div class="quiz-rule quiz-rule--top"></div>
    <div class="timer">
      <svg viewBox="0 0 70 70"><circle cx="35" cy="35" r="32" fill="none" stroke="#050505" stroke-width="2" stroke-dasharray="1.5 3.5"/></svg>
      <div class="timer-value">30</div><div class="timer-unit">SEC</div>
    </div>
    <p class="quiz-copy">This <b>30 second</b> quiz<br>will tell you which procedure<br>will <b>suit you best</b></p>
    <div class="quiz-rule quiz-rule--bottom"></div>
    <div class="contact-label">For all appointments</div>
    <div class="contact-phone">03 9000 4127</div>
    <div class="contact-web">www.marcusbellweather.com.au</div>
  </div>
</section>

</body>
</html>
```